fernbolt website

commerce website to sell cookeries, brackets, mailboxes and to show off homes built. Modern Steel in design see kelvo rides web page to be like: https://www.kelvorides.com/en/ sorry its blue mantis hosting word press divi

must be able to add products to page

Target Market(s)

mainly western states of U.S.

Industry/Entity Type

Building Product

Coding

Coded - Design and coding required

Number of Pages Required

3 page

Font styles to use
Sans Serif

Colors

Designer to choose colors to be used in the design.

Requirements
Must have
• customers to be able to order products from page
• blue mantis hosting word press divi

```html
<!DOCTYPE html>
<html lang="en">
<head>
<meta charset="utf-8">
<title>Fernbolt — Outdoor Steel Products</title>
<link rel="stylesheet" href="https://fonts.googleapis.com/css2?family=Roboto:wght@400;500;700;900&display=swap">
<style>
:root{
  --navy:#2f4a7f;
  --navy-dark:#233a66;
  --ink:#2b2b2b;
  --text:#555;
  --panel:#eeeef6;
  --strip:#f3f3f3;
  --footer:#2b2b30;
  --footer-line:#3c3c42;
  --star:#f0582a;
  --white:#fff;
}
*{margin:0;padding:0;box-sizing:border-box}
html,body{width:1200px;height:4127px;overflow:hidden;background:var(--white)}
body{font-family:'Roboto',sans-serif;color:var(--ink);position:relative}
.abs{position:absolute}
a{color:inherit;text-decoration:none}

/* header */
.site-header{left:0;top:0;width:1200px;height:132px;background:var(--navy)}
.brand{left:143px;top:30px;display:flex;align-items:center;gap:12px;color:var(--white);font-size:30px;font-weight:500;letter-spacing:1px}
.brand-dot{width:34px;height:34px;border-radius:50%;background:var(--white)}
.search{left:588px;top:22px;width:348px;height:39px;border:1px solid #fff;border-radius:3px;background:var(--navy-dark);color:#dfe5f1;font-size:13px;padding:10px 12px}
.search svg{position:absolute;right:12px;top:12px}
.icon-user{left:958px;top:30px}
.icon-cart{left:1013px;top:28px}
.cart-badge{left:1040px;top:26px;width:14px;height:14px;border-radius:50%;background:#fff;color:var(--navy);font-size:9px;text-align:center;line-height:14px;font-weight:700}
.main-nav{top:91px;left:500px;display:flex;gap:0;color:var(--white);font-weight:500;font-size:15px}
.main-nav span{position:absolute;white-space:nowrap}
.nav-active{left:500px;top:127px;width:44px;height:3px;background:#fff}

/* hero */
.hero{left:0;top:132px;width:1200px;height:621px;background:radial-gradient(circle at 35% 35%,#8fb357 0%,#4f7a2a 45%,#2e4f19 100%)}
.hero-grill{left:60px;top:120px;width:500px;height:500px;border-radius:50% 50% 0 0;background:radial-gradient(circle at 50% 35%,#e08a2a 0%,#2a2a2a 45%,rgba(0,0,0,0) 70%)}
.hero-title{left:788px;top:340px;color:var(--white);font-weight:900;line-height:64px;font-size:56px}
.hero-title .big{font-size:70px;line-height:66px}
.btn{display:inline-block;background:var(--navy);color:#fff;font-weight:700;text-align:center;border-radius:3px}
.hero-btn{left:790px;top:550px;width:134px;height:38px;line-height:38px;font-size:14px}
.hero-arrow{width:38px;height:38px;border:2px solid rgba(255,255,255,.8);border-radius:50%}
.hero-arrow svg{position:absolute;left:11px;top:10px}

/* feature strip */
.features{left:0;top:753px;width:1200px;height:168px;background:var(--strip)}
.feature{top:0;height:168px;text-align:center}
.feature h3{font-size:18px;font-weight:500;margin-top:14px;letter-spacing:.5px;color:#222}
.feature p{font-size:13px;color:#444;margin-top:6px}
.feature svg{margin-top:30px}
.feature-divider{top:0;width:1px;height:168px;background:#ddd}

/* category tiles */
.tile{background:var(--panel);overflow:hidden}
.tile h2{position:absolute;font-size:23px;font-weight:700;line-height:34px;color:#222}
.tile .btn{position:absolute;width:114px;height:32px;line-height:32px;font-size:12px}
.tile-img{position:absolute}

/* products */
.products{left:0;top:1690px;width:1200px;height:686px;background:linear-gradient(100deg,#9a9a9a 0%,#e9e9e9 30%,#b3b3b3 55%,#f0f0f0 80%,#a8a8a8 100%)}
.section-title{font-size:37px;font-weight:700;color:#2b2b2b;text-align:center}
.title-rule{height:4px;background:var(--navy)}
.card{top:1900px;width:287px;height:361px;background:#fff;border:1px solid #ddd;text-align:center}
.card-img{position:absolute;left:4px;top:4px;width:277px;height:186px}
.price{position:absolute;left:0;top:210px;width:100%;font-size:18px;font-style:italic;font-weight:500;color:var(--navy)}
.stars{color:var(--star);font-style:normal;letter-spacing:1px;font-size:14px;margin-left:8px}
.card-desc{position:absolute;left:0;top:247px;width:100%;font-size:15px;line-height:23px;color:#333}
.card .btn{position:absolute;left:81px;top:301px;width:125px;height:31px;line-height:31px;font-size:14px;border-radius:16px}

/* feature product */
.feat-img{left:152px;top:2480px;width:449px;height:400px;background:radial-gradient(circle at 50% 60%,#6d6356 0%,#2e2e2e 55%,#6f5138 100%)}
.feat-title{left:641px;top:2503px;font-size:33px;font-weight:700;color:var(--navy);line-height:40px;letter-spacing:.5px}
.feat-price{left:643px;top:2603px;font-size:19px;font-style:italic;font-weight:500;color:var(--navy)}
.body-copy{font-size:14px;line-height:25px;color:#555}
.feat-copy{left:643px;top:2645px;width:405px}
.round-btn{height:38px;line-height:38px;border-radius:19px;font-size:14px;box-shadow:0 3px 6px rgba(0,0,0,.25)}
.feat-btn{left:642px;top:2819px;width:141px}

/* welcome */
.welcome-title{left:144px;top:2967px;font-size:33px;font-weight:700;color:var(--navy)}
.welcome-rule{left:144px;top:3032px;width:54px;height:4px;background:var(--navy)}
.welcome-copy{left:144px;top:3062px;width:410px}
.welcome-btn{left:145px;top:3236px;width:141px}
.welcome-mark{left:596px;top:2996px;width:458px;height:304px;display:flex;flex-direction:column;align-items:center;justify-content:center;gap:18px}
.mark-circle{width:180px;height:180px;border-radius:50%;background:var(--navy)}
.mark-name{font-size:46px;font-weight:700;color:var(--navy);letter-spacing:2px}

/* newsletter */
.newsletter{left:0;top:3400px;width:1200px;height:250px;background:var(--navy);color:#fff;text-align:center}
.ghost{width:230px;height:230px;border-radius:50%;background:rgba(255,255,255,.06);top:10px}
.newsletter h2{position:absolute;left:0;top:42px;width:100%;font-size:37px;font-weight:700;letter-spacing:.5px}
.newsletter p{position:absolute;left:0;top:96px;width:100%;font-size:16px;line-height:24px}
.nl-input{left:327px;top:161px;width:426px;height:39px;border-radius:20px;background:#fff;color:#666;font-size:12px;text-align:left;padding:12px 16px}
.nl-btn{left:758px;top:161px;width:115px;height:39px;border-radius:20px;background:#1e1e22;color:#fff;font-weight:700;font-size:14px;line-height:39px;border:2px solid #45556f}

/* footer */
.site-footer{left:0;top:3650px;width:1200px;height:477px;background:var(--footer);color:#ddd}
.footer-head{font-size:18px;font-weight:500;color:#fff}
.footer-list{font-size:14px;line-height:29px;color:#ccc;list-style:none}
.footer-list li::before{content:"›";margin-right:12px;color:#ccc}
.contact-item{font-size:14px;color:#ddd;line-height:21px;padding-left:37px}
.contact-item svg{position:absolute;left:0;top:2px}
.pay-card{top:91px;width:45px;height:28px;border-radius:3px;background:#dfe3ea}
.social{top:139px;width:32px;height:32px;border:2px solid #ddd;border-radius:50%}
.footer-rule{left:0;top:374px;width:1200px;height:1px;background:var(--footer-line)}
.copyright{left:0;top:418px;width:1200px;text-align:center;font-size:14px;color:#eee}
</style>
</head>
<body>

<header class="abs site-header">
  <div class="abs brand"><span class="brand-dot"></span>FERNBOLT</div>
  <div class="abs search">Search products...
    <svg width="14" height="14" viewBox="0 0 14 14"><circle cx="6" cy="6" r="4.5" fill="none" stroke="#fff" stroke-width="1.6"/><line x1="9.3" y1="9.3" x2="13" y2="13" stroke="#fff" stroke-width="1.6"/></svg>
  </div>
  <svg class="abs icon-user" width="30" height="32" viewBox="0 0 30 32"><circle cx="15" cy="10" r="7" fill="none" stroke="#fff" stroke-width="2"/><path d="M2 30c0-7 6-11 13-11s13 4 13 11z" fill="none" stroke="#fff" stroke-width="2"/></svg>
  <svg class="abs icon-cart" width="34" height="32" viewBox="0 0 34 32"><path d="M1 3h5l4 18h18l4-13H8" fill="none" stroke="#fff" stroke-width="2"/><circle cx="12" cy="27" r="2.5" fill="#fff"/><circle cx="26" cy="27" r="2.5" fill="#fff"/></svg>
  <div class="abs cart-badge">0</div>
  <nav class="abs main-nav" style="left:0;top:91px">
    <span style="left:500px">HOME</span>
    <span style="left:572px">ABOUT US</span>
    <span style="left:678px">OUR PRODUCTS</span>
    <span style="left:822px">SHOP</span>
    <span style="left:892px">BLOG</span>
    <span style="left:961px">CONTACT US</span>
  </nav>
  <div class="abs nav-active"></div>
</header>

<section class="abs hero" role="img" aria-label="Charcoal kettle grill with open flames standing on green lawn">
  <div class="abs hero-grill"></div>
  <div class="abs hero-arrow" style="left:48px;top:288px"><svg width="12" height="14" viewBox="0 0 12 14"><path d="M9 1 3 7l6 6" fill="none" stroke="#fff" stroke-width="2"/></svg></div>
  <div class="abs hero-arrow" style="left:1112px;top:281px"><svg width="12" height="14" viewBox="0 0 12 14"><path d="M3 1l6 6-6 6" fill="none" stroke="#fff" stroke-width="2"/></svg></div>
</section>
<h1 class="abs hero-title">OUTDOOR<br><span class="big">FIREPIT</span><br>COOKERY</h1>
<a class="abs btn hero-btn">SHOP NOW</a>

<section class="abs features">
  <div class="abs feature" style="left:0;width:332px">
    <svg width="44" height="36" viewBox="0 0 44 36"><path d="M3 6h24v20H3zM27 13h8l6 7v6H27z" fill="none" stroke="#2f4a7f" stroke-width="2"/><circle cx="11" cy="28" r="4" fill="#fff" stroke="#2f4a7f" stroke-width="2"/><circle cx="33" cy="28" r="4" fill="#fff" stroke="#2f4a7f" stroke-width="2"/></svg>
    <h3>FREE RETURNS</h3><p>Duis aute irure dolor in</p>
  </div>
  <div class="abs feature-divider" style="left:332px"></div>
  <div class="abs feature" style="left:332px;width:255px">
    <svg width="40" height="36" viewBox="0 0 40 36"><path d="M6 24V18a14 14 0 0 1 28 0v6" fill="none" stroke="#2f4a7f" stroke-width="2"/><rect x="4" y="20" width="8" height="12" rx="3" fill="none" stroke="#2f4a7f" stroke-width="2"/><rect x="28" y="20" width="8" height="12" rx="3" fill="none" stroke="#2f4a7f" stroke-width="2"/></svg>
    <h3>ONLINE SUPPORT</h3><p>Lorem ipsum dolor sit amet</p>
  </div>
  <div class="abs feature-divider" style="left:587px"></div>
  <div class="abs feature" style="left:587px;width:288px">
    <svg width="38" height="38" viewBox="0 0 38 38"><circle cx="19" cy="19" r="17" fill="none" stroke="#2f4a7f" stroke-width="2"/><circle cx="19" cy="19" r="11" fill="none" stroke="#2f4a7f" stroke-width="1.5"/><path d="M19 12v7h5" fill="none" stroke="#2f4a7f" stroke-width="2"/></svg>
    <h3>48 HRS SHIPPING</h3><p>V / booking before kl. 16.30 Mon-Fri</p>
  </div>
  <div class="abs feature-divider" style="left:875px"></div>
  <div class="abs feature" style="left:875px;width:325px">
    <svg width="52" height="34" viewBox="0 0 52 34"><rect x="2" y="4" width="48" height="26" rx="2" fill="none" stroke="#2f4a7f" stroke-width="2"/><rect x="7" y="9" width="38" height="16" fill="none" stroke="#2f4a7f" stroke-width="1.5"/><circle cx="26" cy="17" r="6" fill="none" stroke="#2f4a7f" stroke-width="2"/></svg>
    <h3>EASY PAYMENT</h3><p>For purchases from 499</p>
  </div>
</section>

<!-- category tiles -->
<div class="abs tile" style="left:143px;top:1006px;width:451px;height:280px">
  <div class="tile-img" role="img" aria-label="Steel fire bowl with mesh dome lid on legs" style="left:200px;top:25px;width:235px;height:240px;background:radial-gradient(ellipse at 50% 45%,#3a3a3a 0%,#6d6d72 40%,rgba(238,238,246,0) 70%)"></div>
  <h2 style="left:28px;top:90px">NEMO ENIM<br>VOLUPTATEM</h2>
  <a class="btn" style="left:28px;top:175px">SHOP NOW</a>
</div>
<div class="abs tile" style="left:604px;top:1006px;width:452px;height:280px">
  <div class="tile-img" role="img" aria-label="Round fire pit with mesh dome on curled legs" style="left:20px;top:25px;width:230px;height:240px;background:radial-gradient(ellipse at 50% 45%,#2e2e2e 0%,#5d5d62 40%,rgba(238,238,246,0) 70%)"></div>
  <h2 style="left:274px;top:90px">NEMO ENIM<br>VOLUPTATEM</h2>
  <a class="btn" style="left:274px;top:175px">SHOP NOW</a>
</div>
<div class="abs tile" role="img" aria-label="Kettle grill on grass in bright garden light" style="left:143px;top:1294px;width:451px;height:281px;background:linear-gradient(110deg,#e8efd6 0%,#9fc36a 35%,#4e7a2c 70%,#6b9a3a 100%)">
  <div class="tile-img" style="left:40px;top:150px;width:230px;height:131px;border-radius:50% 50% 0 0;background:#1f2326"></div>
  <h2 style="left:275px;top:65px">NEMO ENIM<br>VOLUPTATEM</h2>
  <a class="btn" style="left:275px;top:150px">SHOP NOW</a>
</div>
<div class="abs tile" style="left:604px;top:1294px;width:452px;height:281px">
  <div class="tile-img" role="img" aria-label="Open fire pit with glowing coals on three legs" style="left:190px;top:30px;width:240px;height:240px;background:radial-gradient(ellipse at 50% 40%,#d9d4cf 0%,#7a726c 35%,#2a2a2a 55%,rgba(238,238,246,0) 72%)"></div>
  <h2 style="left:26px;top:66px">NEMO ENIM<br>VOLUPTATEM</h2>
  <a class="btn" style="left:26px;top:151px">SHOP NOW</a>
</div>

<!-- products -->
<section class="abs products" role="img" aria-label="Brushed steel texture background"></section>
<h2 class="abs section-title" style="left:0;top:1773px;width:1200px">OUR PRODUCTS</h2>
<div class="abs title-rule" style="left:561px;top:1837px;width:77px"></div>

<article class="abs card" style="left:144px">
  <div class="card-img" role="img" aria-label="Steel grill grate over burning fire" style="background:linear-gradient(160deg,#3b3b3b 0%,#6a5c52 50%,#c06a2a 80%,#3a3a3a 100%)"></div>
  <div class="price">$20.58<span class="stars">★★★★★</span></div>
  <p class="card-desc">Nemo enim ipsam voluptatem<br>voluptas sit aspernatur</p>
  <a class="btn">SHOP NOW</a>
</article>
<article class="abs card" style="left:457px">
  <div class="card-img" role="img" aria-label="Kettle grill with flames on green lawn" style="background:radial-gradient(circle at 50% 40%,#c9762a 0%,#2b2b2b 25%,#5f8e2e 45%,#3f6a1c 100%)"></div>
  <div class="price">$20.58<span class="stars">★★★★★</span></div>
  <p class="card-desc">Nemo enim ipsam voluptatem<br>voluptas sit aspernatur</p>
  <a class="btn">SHOP NOW</a>
</article>
<article class="abs card" style="left:769px">
  <div class="card-img" role="img" aria-label="Fire pit with mesh dome burning logs on deck" style="background:radial-gradient(circle at 50% 35%,#d3782b 0%,#3a3330 35%,#8b7a66 75%,#5e544a 100%)"></div>
  <div class="price">$20.58<span class="stars">★★★★★</span></div>
  <p class="card-desc">Nemo enim ipsam voluptatem<br>voluptas sit aspernatur</p>
  <a class="btn">SHOP NOW</a>
</article>

<!-- featured product -->
<div class="abs feat-img" role="img" aria-label="Brushing a kettle grill grate with a blue basting brush"></div>
<h2 class="abs feat-title">BARBEQUE COOKING<br>PRODUCTS</h2>
<div class="abs feat-price">$10.58<span class="stars">★★★★★</span></div>
<p class="abs body-copy feat-copy">Sed ut perspiciatis unde omnis iste natus error sit voluptatem aantium doloremque laudantium, totam rem aperiam, eaque ipsa quae ab illo inventore veritatis et quasi architecto beatae vitae dicta sunt explicabo. Nemo enim ipsam voluptatem quia voluptas sit astur aut odit aut fugit, sed quia consequuntur magni dolores eos qui ratione voluptatem sequi nesciunt.</p>
<a class="abs btn round-btn feat-btn">ADD TO CART</a>

<!-- welcome -->
<h2 class="abs welcome-title">WELCOME TO FERNBOLT</h2>
<div class="abs welcome-rule"></div>
<p class="abs body-copy welcome-copy">Sed ut perspiciatis unde omnis iste natus error sit voluptatem aantium doloremque laudantium, totam rem aperiam, eaque ipsa quae ab illo inventore veritatis et quasi architecto beatae vitae dicta sunt explicabo. Nemo enim ipsam voluptatem quia voluptas sit astur aut odit aut fugit, sed quia consequuntur magni dolores eos qui ratione voluptatem sequi nesciunt.</p>
<a class="abs btn round-btn welcome-btn">LEARN MORE</a>
<div class="abs welcome-mark"><div class="mark-circle"></div><div class="mark-name">FERNBOLT</div></div>

<!-- newsletter -->
<section class="abs newsletter">
  <div class="abs ghost" style="left:50px"></div>
  <div class="abs ghost" style="left:915px"></div>
  <h2>JOIN OUR NEWSLETTER</h2>
  <p>Subscribe to our mailing list to receive updates<br>and promotional offers.</p>
  <div class="abs nl-input">Enter your E - mail</div>
  <div class="abs nl-btn">SUBSCRIBE</div>
</section>

<!-- footer -->
<footer class="abs site-footer">
  <h3 class="abs footer-head" style="left:143px;top:70px">CONTACT US</h3>
  <div class="abs contact-item" style="left:143px;top:118px">
    <svg width="16" height="20" viewBox="0 0 16 20"><path d="M8 1a6.5 6.5 0 0 0-6.5 6.5C1.5 12 8 19 8 19s6.5-7 6.5-11.5A6.5 6.5 0 0 0 8 1z" fill="#fff"/><circle cx="8" cy="7.5" r="2.4" fill="#2b2b30"/></svg>
    ADDRESS<br>123 Street Name, City, England</div>
  <div class="abs contact-item" style="left:143px;top:170px">
    <svg width="17" height="17" viewBox="0 0 17 17"><path d="M3 1l3 .5 1.5 4-2 1.5a10 10 0 0 0 5 5L12 10l4 1.5.5 3c-.5 1.5-2 2-3 2C7 16.5.5 10 .5 3.5c0-1 .8-2.3 2.5-2.5z" fill="#fff"/></svg>
    Phone: (123) 456-7890</div>
  <div class="abs contact-item" style="left:143px;top:202px">
    <svg width="17" height="13" viewBox="0 0 17 13"><rect width="17" height="13" rx="1" fill="#fff"/><path d="M1 1l7.5 6L16 1" fill="none" stroke="#2b2b30" stroke-width="1.4"/></svg>
    E-mail: info@fernbolt.com</div>
  <div class="abs contact-item" style="left:143px;top:235px">
    <svg width="17" height="17" viewBox="0 0 17 17"><circle cx="8.5" cy="8.5" r="8" fill="#fff"/><path d="M8.5 4v5h3.5" fill="none" stroke="#2b2b30" stroke-width="1.6"/></svg>
    Opening hours:<br>Man-Thurs: 9.30-17.30<br>Fri: 9.30-18.00</div>

  <h3 class="abs footer-head" style="left:441px;top:68px">INFORMATION</h3>
  <ul class="abs footer-list" style="left:441px;top:114px">
    <li>Home</li><li>Shop By Brand</li><li>Apparel</li><li>Sell cookeries</li><li>Contact</li>
  </ul>

  <h3 class="abs footer-head" style="left:633px;top:68px">MY ACCOUNT</h3>
  <ul class="abs footer-list" style="left:633px;top:114px">
    <li>Terms &amp; Conditions</li><li>Privacy Policy</li><li>Right of Refusal &amp; Returns</li><li>Cookies</li><li>Shipping &amp; Delivery Terms</li>
  </ul>

  <div class="abs pay-card" style="left:860px"></div>
  <div class="abs pay-card" style="left:910px"></div>
  <div class="abs pay-card" style="left:960px"></div>
  <div class="abs pay-card" style="left:1009px"></div>

  <div class="abs social" style="left:939px"></div>
  <div class="abs social" style="left:981px"></div>
  <div class="abs social" style="left:1022px"></div>

  <div class="abs footer-rule"></div>
  <p class="abs copyright">© 2020 Fernbolt. All Rights Reserved.</p>
</footer>

</body>
</html>
```